Logo + Label Design (Men’s Grooming Brand & Product Packaging)

Design a logo and 2 oz pomade label for Brant, a modern men’s grooming brand focused on clean, high-quality, natural ingredients. The design should establish a bold, masculine, minimalist identity that can later extend to products like shaving gel and body wash.

Key Requirements

Create a primary logo for “Brant” and a core label for the 2 oz pomade jar (screw-top).

Use a clean, modern style — masculine, confident, and approachable (think Wendel’s, Valto, Northfield Mill).

Design for 1–2 color screen printing on solid jar colors (white, black, or navy).

Avoid gradients, foil, or embossing. Must work in black & white.

Provide: vector logo, mockup of the 2 oz jar, color palette (CMYK/RGB/HEX), and font specs.

Winning design may lead to future projects (body wash, shave gel, skincare lines).

Font styles to use
Other font styles liked:
• We like the fonts and design concept in the attached mockup.

Requirements
Should not have
• We want to avoid too much writing or busy designs. We want to avoid having graphics/illustrations embedded in the logo if they will cause the brand to look less classy or sophisticated. We also want the design to look simple and all-American (e.g. Pellham and Stroud, Tall Pine, The BRIM, etc). We’d like to give a Kessler & Dunmore vibe that feels classy and high end.

```html
<!DOCTYPE html>
<html lang="en">
<head>
<meta charset="utf-8">
<title>Brant Hair Pomade – Label</title>
<link href="https://fonts.googleapis.com/css2?family=Montserrat:wght@400;500;600;700;800&display=swap" rel="stylesheet">
<style>
  :root{
    --bg:#202022;
    --jar:#141415;
    --ink:#d9d9d9;
    --ink-soft:#b5b5b5;
    --tan:#9c8d7f;
    --rule:#5a5a5a;
  }
  *{margin:0;padding:0;box-sizing:border-box}
  html,body{width:1200px;height:1000px;overflow:hidden;background:var(--bg)}
  body{position:relative;font-family:"Montserrat",sans-serif;color:var(--ink)}

  .brand-mark{position:absolute;left:34px;top:20px;font-weight:700;font-size:92px;letter-spacing:-2px;color:#f2f2f2;line-height:1}

  /* lid label */
  .lid{position:absolute;left:60px;top:380px;width:480px;height:480px;border-radius:50%;background:var(--jar);
       display:flex;flex-direction:column;align-items:center;justify-content:center;text-align:center}
  .lid .name{font-weight:700;font-size:60px;letter-spacing:-1px;color:var(--ink);line-height:1;margin-bottom:34px}
  .lid .product{font-weight:700;font-size:29px;letter-spacing:3px}
  .lid .scent{font-weight:700;font-size:20px;letter-spacing:1px;margin-top:8px}
  .lid .hold{font-weight:500;font-size:13px;letter-spacing:1px;color:var(--tan);margin-top:30px}
  .lid .weight{font-weight:500;font-size:15px;margin-top:30px}

  /* side wrap label, laid flat */
  .wrap{position:absolute;left:580px;top:330px;width:590px;height:540px;background:var(--jar);border-radius:10px;
        display:grid;grid-template-rows:1fr 1fr}
  .wrap-top{display:grid;grid-template-columns:1fr 1.15fr;gap:26px;padding:34px 28px 20px;border-bottom:1px solid #262626}
  .features p{font-size:12.5px;line-height:1.55;color:var(--ink)}
  .features b{font-weight:700}
  .maker{font-size:9px;color:var(--ink-soft);margin-top:18px;line-height:1.5}
  .icons{display:flex;gap:14px;margin-top:14px}
  .icons svg{width:26px;height:26px}
  .info{font-size:9.5px;line-height:1.45;color:var(--ink-soft)}
  .info h4{font-size:10px;font-weight:700;color:var(--ink);display:inline}
  .info .direction{margin-top:12px}
  .external{margin-top:12px;font-size:11px;font-weight:700;color:var(--ink)}
  .external-box{margin-top:4px;border:1px solid var(--rule);border-radius:3px;padding:3px 6px;font-size:8.5px;color:var(--ink-soft);font-weight:400}

  .front{padding:36px 40px}
  .front .name{font-weight:700;font-size:38px;letter-spacing:-1px;line-height:1}
  .front .product{font-weight:700;font-size:22px;letter-spacing:2.5px;margin-top:12px}
  .front .scent{font-weight:700;font-size:15px;letter-spacing:1px;margin-top:8px}
  .front .rule{height:1px;background:var(--rule);margin-top:20px;width:420px}
  .front .row{display:flex;justify-content:space-between;width:420px;margin-top:10px;font-size:11px;letter-spacing:1px}
  .front .hold{color:var(--tan);font-weight:500}
  .front .weight{font-weight:500}
</style>
</head>
<body>
  <div class="brand-mark">Brant.</div>

  <section class="lid">
    <div class="name">Brant.</div>
    <div class="product">HAIR POMADE</div>
    <div class="scent">FRESH &amp; CLEAN</div>
    <div class="hold">MEDIUM HOLD | MATTE FINISH</div>
    <div class="weight">&#8494; 2 oz | 57 g</div>
  </section>

  <section class="wrap">
    <div class="wrap-top">
      <div class="features">
        <p>Natural <b>plant &amp; bee-based</b> ingredients</p>
        <p>Non-irritating</p>
        <p>Helps minimize scalp irritation</p>
        <div class="maker">Made for Brant Goods, Ashford, NC 27514<br>brantgoods.com</div>
        <div class="icons">
          <svg viewBox="0 0 26 26" fill="none" stroke="#d9d9d9" stroke-width="1.5"><circle cx="13" cy="13" r="11"/><line x1="5" y1="21" x2="21" y2="5"/></svg>
          <svg viewBox="0 0 26 26" fill="none" stroke="#d9d9d9" stroke-width="1.5"><path d="M4 10h18v12H4z"/><path d="M6 10l2-5h12"/><text x="13" y="19.5" font-size="6" fill="#d9d9d9" stroke="none" text-anchor="middle" font-family="Montserrat,sans-serif">24M</text></svg>
          <svg viewBox="0 0 26 26" fill="none" stroke="#d9d9d9" stroke-width="1.6"><path d="M13 4l-5 8M9 12H5l3-5"/><path d="M22 17l-5-8M21 13l1 4-4 0"/><path d="M5 20h14M16 17l3 3-3 3"/></svg>
        </div>
      </div>
      <div class="info">
        <p>Ingredients : Butyrospermum Parkii (Shea Butter), Cera Alba (Beeswax), Polyglycerol-3 Beeswax (Cera Bellina), Caprylic/Capric Triglyceride (Fractionated Coconut Oil), Tocopherol (Vitamin E), Fragrance (Parfum)</p>
        <p class="direction"><h4>Direction :</h4> Melt small amount of pomade between hands before massaging into damp hair (for sleeker look) or dry hair (for more texture). Style as desired. For external use only. Avoid contact with eyes. If irritation occurs, discontinue use.</p>
        <div class="external">For external use only
          <div class="external-box">Avoid contact with eyes | Keep out of reach of children</div>
        </div>
      </div>
    </div>
    <div class="front">
      <div class="name">Brant.</div>
      <div class="product">HAIR POMADE</div>
      <div class="scent">FRESH &amp; CLEAN</div>
      <div class="rule"></div>
      <div class="row"><span class="hold">MEDIUM HOLD | MATTE FINISH</span><span class="weight">&#8494; 2 oz | 57 g</span></div>
    </div>
  </section>
</body>
</html>
```